Flyer-Design für Pultrusionstechnologie
Zielgruppe
Wir sind eine europäische Vereinigung von Herstellern mit Pultrusionstechnologie. Unser Ziel ist, die Pultrusionstechnik bekannter zu machen, für Kunststoffhersteller und Kunden.
Aufgabenstellung
Der Text im Flyer ist von uns vorgegeben. Das Format des Flyers soll klassisch sein, A4, zweimal gefaltet.

```html
<!DOCTYPE html>
<html lang="en">
<head>
<meta charset="utf-8">
<title>Profile Forum Europe – Tri-fold Flyer</title>
<link href="https://fonts.googleapis.com/css2?family=Raleway:ital,wght@0,400;0,500;0,700;0,800;1,800&family=Caveat:wght@500&display=swap" rel="stylesheet">
<style>
  :root{
    --blue:#5589c4;
    --blue-head:#3f78bf;
    --blue-deep:#1f5fae;
    --orange:#f0963f;
    --text:#2b2b2b;
    --dark:#2e2e2e;
    --paper:#ffffff;
    --bg:#ffffff;
    --divider:#cfd4da;
  }
  *{box-sizing:border-box;margin:0;padding:0}
  html,body{width:800px;height:1200px;overflow:hidden;background:var(--bg)}
  body{position:relative;font-family:"Raleway",Arial,sans-serif;color:var(--text)}
  .abs{position:absolute}

  .brand-name{font-family:"Raleway",Arial,sans-serif;font-weight:800;color:var(--blue-deep);display:flex;align-items:center;gap:6px;white-space:nowrap}
  .brand-name .mark{display:inline-block;background:currentColor}
  .brand-top{left:0;width:800px;top:46px;justify-content:center;font-size:22px}
  .brand-top .mark{width:16px;height:16px}

  .spread{position:absolute;left:57px;width:679px;background:var(--paper);box-shadow:0 3px 8px rgba(0,0,0,.18)}
  .spread-outside{top:120px;height:480px}
  .spread-inside{top:633px;height:480px}
  .fold{position:absolute;width:0;border-left:1px dashed var(--divider)}

  .heading{position:absolute;font-weight:800;font-size:6.6px;letter-spacing:.5px;color:var(--blue-head);text-transform:uppercase}
  .copy{position:absolute;font-size:6.5px;line-height:11.4px;color:var(--text)}
  .copy p+p{margin-top:6.5px}

  .photo{position:absolute}
  .photo-machine{background:linear-gradient(135deg,#dfe9f5,#8fb0d6 55%,#4f7fb8)}
  .photo-profiles{background:linear-gradient(160deg,#e9eef5 0%,#a9bfdc 45%,#2d4f86 80%,#0f1f3c 100%)}
  .photo-pipes{background:radial-gradient(circle at 40% 30%,#f6d57a,#3f8fc4 60%,#163c66)}
  .photo-steel{background:linear-gradient(135deg,#cfdcee,#3b6fb3 60%,#15315e)}

  .sponsor{position:absolute;width:32px;height:8px;border-radius:2px;background:#9fb7d6}

  .panel-contact{position:absolute;left:221px;top:173px;width:230px;height:307px;background:var(--blue);color:#fff}
  .script{font-family:"Caveat",cursive;font-weight:500}
  .advise{position:absolute;left:0;width:230px;top:40px;text-align:center;font-size:14px;transform:rotate(-4deg);color:#fff}
  .brand-white{position:absolute;left:12px;top:91px;color:#fff;font-size:13px}
  .brand-white .mark{width:12px;height:12px}
  .contact-line{position:absolute;left:82px;font-size:6.4px;letter-spacing:.5px;line-height:11.3px;color:#fff}
  .contact-icon{position:absolute;left:61px;width:9px;height:9px;border-radius:2px;background:var(--orange)}

  .overlay-box{position:absolute;left:18px;top:18px;width:139px;height:128px;background:rgba(63,120,191,.88);color:#fff;padding:10px 10px}
  .overlay-title{font-weight:800;font-style:italic;font-size:13px;line-height:16.5px}
  .overlay-text{font-size:8.3px;line-height:10px;margin-top:7px}

  .brand-cover{position:absolute;left:485px;top:82px;font-size:12.5px}
  .brand-cover .mark{width:11px;height:11px}
  .cover-tag{position:absolute;left:451px;width:228px;top:120px;text-align:center;color:var(--orange);font-size:13px;transform:rotate(-4deg)}

  .diagram{position:absolute;left:22px;top:195px;width:416px;height:90px;background:linear-gradient(180deg,#f4f6f9,#e6ebf1);border-bottom:1px solid #3a3a3a}
  .callout{position:absolute;color:#fff;padding:7px 9px}
  .callout-blue{background:var(--blue)}
  .callout-orange{background:var(--orange)}
  .callout h3{font-weight:800;font-size:6.3px;letter-spacing:.5px}
  .callout p{font-size:6.4px;line-height:7.8px;margin-top:7px}
  .label{position:absolute;color:var(--orange);font-weight:700;font-size:7.5px;border-bottom:1px solid var(--blue);padding-bottom:1px}
  .leaders{position:absolute;left:0;top:0}

  .benefits{position:absolute;left:479px;top:90px;list-style:none;font-size:6.4px;line-height:11.35px}
  .benefits li::before{content:"+";color:var(--orange);margin-right:6px}

  .footer-bar{position:absolute;left:0;bottom:0;width:679px;height:22px;background:var(--dark)}
  .footer-url{position:absolute;top:7px;font-size:4.6px;font-weight:700;color:#fff;transform:translateX(-50%)}
</style>
</head>
<body>

<div class="brand-name brand-top abs"><span class="mark"></span>Profile Forum Europe</div>

<!-- Outside spread -->
<section class="spread spread-outside">
  <div class="fold" style="left:221px;top:0;height:173px"></div>
  <div class="fold" style="left:451px;top:0;height:173px"></div>

  <div class="photo photo-machine" style="left:24px;top:24px;width:173px;height:120px" role="img" aria-label="Photo of a pultrusion machine with fibre rolls"></div>

  <h2 class="heading" style="left:22px;top:166px">About PFE</h2>
  <div class="copy" style="left:22px;top:181px;width:180px">
    <p>PFE is Profile Forum Europe, the association of composite profile makers. It was created in 1989 by the leading Pultruders in Europe. With today 40 member companies/institutions PFE is the largest pultrusion network in Europe. The mission is to support the growth of the composite profiles industry by maximizing external communication efforts and having an actively contributing membership.</p>
    <p>PFE is open for membership to all companies and organizations, wishing to participate in promoting the responsible use of Fiber Reinforced Composite Materials, and in the exchange of knowledge between members.</p>
  </div>

  <h2 class="heading" style="left:22px;top:329px">Sponsor Members</h2>
  <span class="sponsor" style="left:22px;top:349px"></span>
  <span class="sponsor" style="left:73px;top:349px"></span>
  <span class="sponsor" style="left:125px;top:349px"></span>
  <span class="sponsor" style="left:176px;top:349px"></span>
  <span class="sponsor" style="left:22px;top:369px"></span>
  <span class="sponsor" style="left:73px;top:369px"></span>
  <span class="sponsor" style="left:133px;top:365px;width:16px;height:14px"></span>
  <span class="sponsor" style="left:176px;top:367px;height:11px;border-radius:6px"></span>

  <h2 class="heading" style="left:244px;top:23px">Additional Information</h2>
  <div class="copy" style="left:244px;top:40px;width:190px">
    <p>You want to know more about pultrusion, technical specifications or our members? Please visit our website www.profileforum.eu.</p>
    <p>Find news articles, background documents and the largest pultrusion network in Europe. We are looking forward to your visit!</p>
  </div>

  <div class="brand-name brand-cover"><span class="mark"></span>Profile Forum Europe</div>
  <div class="cover-tag script">Lorem ipsum dolor!</div>

  <div class="panel-contact">
    <div class="advise script">We will gladly advise you!</div>
    <div class="brand-name brand-white"><span class="mark"></span>Profile Forum Europe</div>

    <svg class="contact-icon" style="top:159px" viewBox="0 0 10 10" aria-hidden="true"><rect width="10" height="10" rx="2" fill="#f0963f"/><path d="M5 2a2 2 0 0 1 2 2c0 1.5-2 4-2 4S3 5.5 3 4a2 2 0 0 1 2-2z" fill="#fff"/></svg>
    <div class="contact-line" style="top:152px">Werkstraße 18<br>50667 Köln<br>GERMANY</div>

    <svg class="contact-icon" style="top:196px" viewBox="0 0 10 10" aria-hidden="true"><rect width="10" height="10" rx="2" fill="#f0963f"/><path d="M3 2.5l1.2-.3.8 1.6-.8.6c.4.9 1 1.5 1.9 1.9l.6-.8 1.6.8-.3 1.2C5.7 7.6 2.4 4.3 3 2.5z" fill="#fff"/></svg>
    <svg class="contact-icon" style="top:207px" viewBox="0 0 10 10" aria-hidden="true"><rect width="10" height="10" rx="2" fill="#f0963f"/><rect x="3" y="2.5" width="4" height="2" fill="#fff"/><rect x="2.3" y="4.8" width="5.4" height="2.5" fill="#fff"/></svg>
    <div class="contact-line" style="top:197px">Tel: (49) 221-48 30 55 – 0<br>Fax: (49) 221-48 30 55 – 10</div>

    <svg class="contact-icon" style="top:231px" viewBox="0 0 10 10" aria-hidden="true"><rect width="10" height="10" rx="2" fill="#f0963f"/><circle cx="5" cy="5" r="2.6" fill="none" stroke="#fff" stroke-width="1"/><circle cx="5" cy="5" r="1" fill="#fff"/></svg>
    <svg class="contact-icon" style="top:242px" viewBox="0 0 10 10" aria-hidden="true"><rect width="10" height="10" rx="2" fill="#f0963f"/><circle cx="5" cy="5" r="2.8" fill="none" stroke="#fff" stroke-width=".8"/><path d="M2.2 5h5.6M5 2.2v5.6" stroke="#fff" stroke-width=".7"/></svg>
    <div class="contact-line" style="top:231px">info@profileforum.eu<br>www.profileforum.eu</div>
  </div>

  <div class="photo photo-profiles" style="left:451px;top:173px;width:228px;height:307px" role="img" aria-label="Photo of stacked white pultruded profiles">
    <div class="overlay-box">
      <div class="overlay-title">Lorem ipsum<br>dolor elit!<br>Pidus atemolorit.</div>
      <div class="overlay-text">optaqui scimus modit, solo qui aligni con none doloribeat et ditaturerum doleni cuptat. aligni con none doloribeat et ditaturerum doleni cuptat.</div>
    </div>
  </div>
</section>

<!-- Inside spread -->
<section class="spread spread-inside">
  <div class="fold" style="left:228px;top:0;height:458px"></div>
  <div class="fold" style="left:457px;top:0;height:458px"></div>

  <h2 class="heading" style="left:22px;top:24px">What is Pultrusion?</h2>
  <div class="copy" style="left:22px;top:40px;width:186px">
    <p>Pultrusion is an automated process for the continuous production of FRP (Fiber Reinforced Plastics) profiles with a constant cross section. The process is very well established with nearly unlimited possibilities. In the process, the use of various materials/semi-finished products is possible.</p>
  </div>

  <div class="diagram" role="img" aria-label="Line drawing of a pultrusion line from creel to cutting saw"></div>

  <svg class="leaders" width="679" height="480" aria-hidden="true">
    <g fill="none" stroke="#5589c4" stroke-width=".8">
      <path d="M49 196h52l12 26"/><circle cx="113" cy="223" r="1.6" fill="#fff"/>
      <path d="M246 186h-29l-11 24"/><circle cx="206" cy="211" r="1.6" fill="#fff"/>
      <path d="M408 206h-55l-12 23"/><circle cx="341" cy="229" r="1.6" fill="#fff"/>
      <path d="M359 316h31l11-26"/><circle cx="401" cy="290" r="1.6" fill="#fff"/>
    </g>
    <g fill="none" stroke="#f0963f" stroke-width=".8">
      <path d="M153 331h92l32-74"/><circle cx="278" cy="256" r="1.6" fill="#fff"/>
    </g>
  </svg>

  <span class="label" style="left:49px;top:185px">Lorem ipsum</span>
  <span class="label" style="left:356px;top:195px">Lorem ipsum</span>

  <div class="callout callout-blue" style="left:246px;top:125px;width:77px;height:76px">
    <h3>LOREM IPSUM</h3>
    <p>Lorem ipsum dolor sit amet, consetetur sadipscing elitr, sed diam nonumy eirmod tempor invidunt ut labore.</p>
  </div>
  <div class="callout callout-orange" style="left:22px;top:307px;width:131px;height:101px">
    <h3>LOREM IPSUM</h3>
    <p>Lorem ipsum dolor Lorem ipsum dolor sit amet, consetetur sadipscing elitr, sed diam nonumy eirmod tempor invidunt ut labore et dolore magna aliquyam erat, sed diam voluptua. At vero eos et accusam et justo duo dolores et ea rebum. Stet clita kasd gubergren, no sea takimata sanctus est voluptua.</p>
  </div>
  <div class="callout callout-blue" style="left:282px;top:307px;width:77px;height:76px">
    <h3>LOREM IPSUM</h3>
    <p>Lorem ipsum dolor sit amet, consetetur sadipscing elitr, sed diam nonumy eirmod tempor invidunt ut labore.</p>
  </div>

  <h2 class="heading" style="left:479px;top:24px">Advantages of Pultrusion</h2>
  <div class="copy" style="left:479px;top:40px;width:185px">
    <p>FRP-Profiles are perfect materials for the construction of structural elements.<br>There are several advantages (e.g.):</p>
  </div>
  <ul class="benefits">
    <li>Nearly no limitations in shape or length</li>
    <li>High lightweight potential (low density)</li>
    <li>Very high tensile strength</li>
    <li>Profiles are easy to transport and to install</li>
    <li>Corrosion and weather resistant</li>
    <li>Excellent chemical and biological resistance</li>
    <li>Nearly Maintenance free usage</li>
    <li>Low thermal and electrical conductivity (GFRP)</li>
    <li>Transparent to electromagnetic waves</li>
  </ul>

  <h2 class="heading" style="left:479px;top:208px">Typical Applications</h2>
  <div class="copy" style="left:479px;top:224px;width:185px">
    <p>FRP profiles are predestined for use in a challenging environment. The high-performance potential and outstanding properties have made FRP profiles the material of choice in many applications &amp; industries. Today you will find profiles in building- und infrastructure sector, sports- and leisure, mobility, wind-industry and many more.</p>
  </div>

  <div class="photo photo-steel" style="left:479px;top:313px;width:84px;height:57px" role="img" aria-label="Photo of profiles on a production line"></div>
  <div class="photo photo-pipes" style="left:572px;top:313px;width:84px;height:57px" role="img" aria-label="Photo of stacked composite tubes"></div>
  <div class="photo photo-machine" style="left:479px;top:380px;width:84px;height:58px" role="img" aria-label="Photo of a pultrusion machine with fibre rolls"></div>
  <div class="photo photo-steel" style="left:572px;top:380px;width:84px;height:58px" role="img" aria-label="Photo of a composite structure in perspective"></div>

  <footer class="footer-bar">
    <span class="footer-url" style="left:114px">www.profileforum.eu</span>
    <span class="footer-url" style="left:342px">www.profileforum.eu</span>
    <span class="footer-url" style="left:568px">www.profileforum.eu</span>
  </footer>
</section>

</body>
</html>
```